International service dog training school needs web design

We need to upgrade our website. The website is https://brightpathmentor.site/
We help trainers and service dog programs learn how to train service dogs with the latest and most ethical training methods. We offer online and in-person coaching services. We would like to see designs that are engaging and communicate professionalism, expertise, and care for the dogs and people we work with. Please also keep the colors already in the logo in the design.

```html
<!DOCTYPE html>
<html lang="en">
<head>
<meta charset="utf-8">
<title>Brightpath Mentor Center – Coaching for Service Dog Professionals</title>
<link rel="stylesheet" href="https://fonts.googleapis.com/css2?family=Poppins:wght@400;500;600;700;800&family=Open+Sans:wght@400;600&display=swap">
<style>
:root{
  --teal:#15a99a;
  --teal-dark:#0f9486;
  --blue:#1d6fc0;
  --blue-dark:#165fa8;
  --navy:#0f1c3a;
  --ink:#111;
  --text:#333;
  --muted:#666;
  --sky:#a9d3f4;
  --card:#f6f7f8;
  --white:#fff;
}
*{box-sizing:border-box;margin:0;padding:0}
html,body{width:1200px;height:3267px;overflow:hidden}
body{font-family:"Open Sans",sans-serif;color:var(--text);background:var(--white);position:relative}
.section{position:absolute;left:0;width:1200px}
.abs{position:absolute}
.btn{position:absolute;display:flex;align-items:center;justify-content:center;border-radius:16px;color:var(--white);font-family:"Poppins",sans-serif;font-size:11px;font-weight:400;text-transform:uppercase;letter-spacing:.2px;text-decoration:none;white-space:nowrap}
.btn--teal{background:var(--teal)}
.btn--blue{background:var(--blue)}
.photo{position:absolute}

/* top bar */
.topbar{top:0;height:32px;background:var(--teal);color:var(--white);font-size:10.5px}
.topbar__item{position:absolute;top:0;height:32px;display:flex;align-items:center;gap:8px}
/* nav */
.nav{top:32px;height:54px;background:#0d0d0d}
.brand{position:absolute;left:250px;top:0;height:54px;display:flex;align-items:center;gap:9px}
.brand__dot{width:34px;height:34px;border-radius:50%;background:var(--teal);flex:none}
.brand__name{font-family:"Poppins",sans-serif;font-weight:600;font-size:15px;color:var(--white);line-height:1.15}
.menu{position:absolute;right:256px;top:0;height:54px;display:flex;align-items:center;gap:13px;font-family:"Poppins",sans-serif;font-size:10px;color:var(--white);text-transform:uppercase;white-space:nowrap}
.menu__sep{width:1px;height:16px;background:#888;margin:0 4px}
/* hero */
.hero{top:86px;height:374px}
.hero__photo{left:0;top:0;width:1200px;height:374px;background:linear-gradient(90deg,#14234d 0%,#1f3a82 45%,#27428d 70%,#1a2c60 100%)}
.hero__title{left:250px;top:62px;font-family:"Poppins",sans-serif;font-weight:700;font-size:39px;line-height:44px;color:var(--white);white-space:nowrap}
.hero__lead{left:250px;top:154px;width:390px;font-size:20px;line-height:24px;color:var(--white)}
.hero__lead mark{background:var(--teal);color:var(--white);padding:0 2px}

/* offer box */
.offer{top:504px;left:250px;width:701px;height:248px;background:var(--blue);border-radius:4px}
.offer__card{position:absolute;top:18px;width:324px;height:212px;border-radius:8px;background:#5b9ad6;padding:9px}
.offer__img{width:100%;height:100%;border-radius:2px}
.offer__pill{position:absolute;left:26px;bottom:20px;width:288px;height:30px;border-radius:15px;background:var(--teal);color:var(--white);font-family:"Poppins",sans-serif;font-size:10.5px;display:flex;align-items:center;padding-left:18px;text-transform:uppercase;white-space:nowrap}
.offer__arrow{position:absolute;right:6px;top:4px;width:22px;height:22px;border-radius:50%;border:2px solid var(--white)}

/* research */
.h2{position:absolute;left:0;width:1200px;text-align:center;font-family:"Poppins",sans-serif;font-weight:700;color:var(--ink)}
.rule{position:absolute;left:539px;width:122px;height:2px;background:var(--blue)}
.rule::after{content:"";position:absolute;left:46px;top:-1px;width:30px;height:4px;background:var(--teal);border-radius:2px}
.sub{position:absolute;left:0;width:1200px;text-align:center;font-family:"Poppins",sans-serif;font-size:11px;color:var(--teal)}
.para{position:absolute;left:285px;width:630px;text-align:center;font-size:9.6px;line-height:14.5px;color:#444}
.video{left:424px;top:977px;width:352px;height:198px;background:linear-gradient(160deg,#5d6a78,#2c3440 60%,#8a9198);border:1px solid #333}
.video__title{position:absolute;left:18px;top:6px;color:var(--white);font-size:6px}
.video__play{position:absolute;left:156px;top:80px;width:40px;height:28px;border-radius:50%;background:#111}

/* services */
.services{top:1218px;height:529px;background:var(--sky)}
.svc{position:absolute;width:222px;height:213px;border-radius:3px;overflow:hidden;background:var(--blue)}
.svc__img{height:168px}
.svc__label{position:absolute;left:0;bottom:0;width:100%;height:45px;background:var(--blue);color:var(--white);font-family:"Poppins",sans-serif;font-weight:600;font-size:11px;line-height:12.5px;padding:10px 18px 0}

/* courses */
.course{position:absolute;width:222px;height:301px;background:var(--card)}
.course__img{height:136px;position:relative}
.course__price{position:absolute;right:0;bottom:22px;width:72px;height:28px;border-radius:14px 0 0 14px;background:var(--teal);color:var(--white);font-size:11px;display:flex;align-items:center;justify-content:center}
.course__title{position:absolute;top:152px;left:0;width:100%;text-align:center;font-family:"Poppins",sans-serif;font-weight:600;font-size:10.5px;line-height:14px;color:var(--ink)}
.course__incl{position:absolute;top:205px;left:0;width:100%;text-align:center;font-size:11px;color:var(--teal);display:flex;justify-content:center;align-items:center;gap:4px}
.course__meta{position:absolute;top:230px;left:0;width:100%;display:flex;justify-content:center;gap:28px;font-size:9.5px;color:#555}
.course__meta span{display:flex;align-items:center;gap:5px}
.course .btn{left:37px;top:256px;width:148px;height:26px}

/* book */
.book-band{top:2641px;height:197px;background:var(--teal)}
.book__cover{left:375px;top:2505px;width:203px;height:298px;background:linear-gradient(180deg,#f4f1ea 0%,#efe9dc 45%,#c9a56a 60%,#7c2226 100%)}
.book__spine{left:251px;top:2505px;width:124px;height:300px;background:linear-gradient(90deg,#d7d7d7,#fafafa 40%,#e2e2e2);clip-path:polygon(80% 0,100% 0,100% 100%,0 100%,0 94%)}
.reviews{left:621px;top:2508px}
.reviews__title{font-family:"Poppins",sans-serif;font-weight:600;font-size:15.5px;color:var(--ink)}
.stars{display:flex;gap:4px;margin-top:8px}
.stars span{width:24px;height:24px;background:#f29a16;display:flex;align-items:center;justify-content:center}
.reviews__score{font-size:8px;margin:7px 0 0 48px;color:#222}
.reviews__market{font-family:"Poppins",sans-serif;font-weight:700;font-size:32px;color:var(--ink);line-height:38px;margin-top:2px}
.book__title{left:626px;top:2677px;font-family:"Poppins",sans-serif;font-weight:700;font-size:25px;line-height:29px;color:var(--white);white-space:nowrap}
.book__text{left:626px;top:2742px;width:290px;font-size:9.5px;line-height:14px;color:var(--white)}

/* footer */
.footer{top:3028px;height:213px;background:var(--teal);color:var(--white)}
.footer__brand{left:250px;top:24px;display:flex;align-items:center;gap:9px}
.footer__about{left:250px;top:84px;width:206px;font-size:9.6px;line-height:15px}
.socials{left:250px;top:178px;display:flex;gap:7px}
.socials span{width:20px;height:20px;border-radius:50%;background:var(--white)}
.links{position:absolute;top:28px;list-style:none;font-size:11px;line-height:23.5px}
.links li{display:flex;align-items:center;gap:8px}
.links li::before{content:"";width:9px;height:9px;border-radius:50%;border:2px solid var(--white);box-sizing:border-box}
.bottom{top:3241px;height:26px;background:var(--blue-dark);color:var(--white);font-size:8px}
</style>
</head>
<body>

<div class="section topbar">
  <div class="topbar__item" style="left:250px">
    <svg width="11" height="11" viewBox="0 0 24 24" fill="#fff"><path d="M6.6 10.8a15.1 15.1 0 0 0 6.6 6.6l2.2-2.2c.3-.3.7-.4 1-.2 1.1.4 2.3.6 3.6.6.6 0 1 .4 1 1V20c0 .6-.4 1-1 1A17 17 0 0 1 3 4c0-.6.4-1 1-1h3.5c.6 0 1 .4 1 1 0 1.3.2 2.5.6 3.6.1.3 0 .7-.2 1z"/></svg>
    1234567890
  </div>
  <div class="topbar__item" style="left:810px">
    <svg width="13" height="10" viewBox="0 0 24 18" fill="#fff"><path d="M2 0h20a2 2 0 0 1 2 2v.5l-12 7-12-7V2a2 2 0 0 1 2-2zm-2 4.8 12 7 12-7V16a2 2 0 0 1-2 2H2a2 2 0 0 1-2-2z"/></svg>
    info@brightpathmentor.site
  </div>
</div>

<nav class="section nav">
  <div class="brand"><span class="brand__dot"></span><span class="brand__name">Brightpath<br>Mentor Center</span></div>
  <div class="menu">
    <span>The Center</span><span>Helping Organizations</span><span>Teaching Trainers</span><span>Research</span><span>Contact Us</span>
    <span class="menu__sep"></span>
    <svg width="12" height="12" viewBox="0 0 24 24" fill="none" stroke="#fff" stroke-width="3"><circle cx="10" cy="10" r="7"/><path d="M15 15l7 7"/></svg>
  </div>
</nav>

<header class="section hero">
  <div class="photo hero__photo" role="img" aria-label="Trainer walking a large service dog on leash through an indoor training hall with agility poles"></div>
  <h1 class="abs hero__title">Coaching For Service<br>Dog Professionals</h1>
  <p class="abs hero__lead">The Brightpath Mentor Center, <mark>Click Below</mark> for a list of courses offered and the Brightpath Mentor Center.</p>
  <a class="btn btn--teal" style="left:250px;top:279px;width:147px;height:27px">Click here for list</a>
  <a class="btn btn--blue" style="left:410px;top:279px;width:147px;height:27px">Contact us</a>
</header>

<section class="section offer">
  <div class="offer__card" style="left:18px">
    <div class="photo offer__img" style="position:static;background:linear-gradient(180deg,#6c7c8c,#9c8f78)" role="img" aria-label="Group of trainers with dogs during outdoor in-person teaching"></div>
    <div class="offer__pill">In-person teaching at your facility<span class="offer__arrow"></span></div>
  </div>
  <div class="offer__card" style="left:360px">
    <div class="photo offer__img" style="position:static;background:linear-gradient(180deg,#9ea6ae,#6e6f70)" role="img" aria-label="Trainers working with dogs in an airport waiting area"></div>
    <div class="offer__pill">In-person learning at our facility<span class="offer__arrow"></span></div>
  </div>
</section>

<h2 class="h2" style="top:787px;font-size:24px">Medical Detection Dogs - Research Projects</h2>
<div class="rule" style="top:830px"></div>
<p class="sub" style="top:846px">Expertise and collaboration with your research projects</p>
<p class="para" style="top:876px">Marianne Holloway Ph.D. is involved in different research projects in the area of medical detection dogs. She has been at the forefront of canine medical detection research and development projects. Her work involves proving the ability of dogs to detect the scent of hypoglycemic episodes as well as seizures.</p>
<p class="para" style="top:933px">If you have a specific interest in the field of medical detection that could benefit from external oversight or from collaboration and trained dogs, consider contacting the Brightpath Mentor Center (BMC).</p>
<div class="photo video" role="img" aria-label="Video still of a detection dog sniffing scent cans on a training floor">
  <span class="video__title">Research in practice: scent detection trials</span>
  <span class="video__play"><svg width="40" height="28" viewBox="0 0 40 28"><path d="M16 8l10 6-10 6z" fill="#fff"/></svg></span>
</div>

<section class="section services" aria-label="Services">
  <div class="svc" style="left:250px;top:40px"><div class="photo svc__img" style="position:static;background:linear-gradient(180deg,#8a8a86,#4e5a6a)" role="img" aria-label="Program staff posing together with their dogs"></div><div class="svc__label">Organization/Program<br>Consulting</div></div>
  <div class="svc" style="left:489px;top:40px"><div class="photo svc__img" style="position:static;background:linear-gradient(180deg,#d7d6d2,#7a6656)" role="img" aria-label="Trainer coaching with treat pouch"></div><div class="svc__label">Professional coaching/teaching<br>for dog trainers</div></div>
  <div class="svc" style="left:729px;top:40px"><div class="photo svc__img" style="position:static;background:linear-gradient(180deg,#c9c5bd,#9a948a)" role="img" aria-label="Detection dog in vest sniffing a can"></div><div class="svc__label">Collaborating in Research<br>Projects</div></div>
  <div class="svc" style="left:369px;top:272px"><div class="photo svc__img" style="position:static;background:linear-gradient(180deg,#d4d3cf,#45403c)" role="img" aria-label="Audience at a seminar presentation"></div><div class="svc__label">Presentations and<br>Seminars</div></div>
  <div class="svc" style="left:609px;top:272px"><div class="photo svc__img" style="position:static;background:linear-gradient(180deg,#c9ced6,#5a4a40)" role="img" aria-label="Service dog looking out an airport window"></div><div class="svc__label">International<br>Services</div></div>
</section>

<h2 class="h2" style="top:1778px;font-size:24px">Popular Courses</h2>
<div class="rule" style="top:1821px"></div>

<div class="course" style="left:250px;top:1843px">
  <div class="photo course__img" style="position:relative;background:linear-gradient(180deg,#b8b9bc,#5c5450)" role="img" aria-label="Trainers walking service dogs in a hallway"><span class="course__price">$3,500</span></div>
  <div class="course__title">Full Curriculum - All You Need To<br>Train a Medical Assistant Dog</div>
  <div class="course__incl">☆ Included In Subscription ☆</div>
  <div class="course__meta"><span>▭ Online</span><span>◎ Certificate</span></div>
  <a class="btn btn--teal">See course detail</a>
</div>
<div class="course" style="left:489px;top:1843px">
  <div class="photo course__img" style="position:relative;background:linear-gradient(180deg,#cfc7b8,#8d7a62)" role="img" aria-label="Dogs waiting in kennel runs"><span class="course__price">$850</span></div>
  <div class="course__title">Service Dog Candidate<br>Selection</div>
  <div class="course__incl">☆ Included In Subscription ☆</div>
  <div class="course__meta"><span>▭ Online</span><span>◎ Certificate</span></div>
  <a class="btn btn--blue">See course detail</a>
</div>
<div class="course" style="left:729px;top:1843px">
  <div class="photo course__img" style="position:relative;background:linear-gradient(180deg,#c9c3b4,#7a5e4c)" role="img" aria-label="Class of trainers in a classroom"><span class="course__price">$1,250</span></div>
  <div class="course__title">Service Dog Training<br>and Assessments</div>
  <div class="course__incl">☆ Included In Subscription ☆</div>
  <div class="course__meta"><span>▭ Online</span><span>◎ Certificate</span></div>
  <a class="btn btn--teal">See course detail</a>
</div>
<div class="course" style="left:250px;top:2161px">
  <div class="photo course__img" style="position:relative;background:linear-gradient(180deg,#d9d5cc,#7a5f42)" role="img" aria-label="Dog performing a task beside a trainer"><span class="course__price">$1,250</span></div>
  <div class="course__title">Medical Assistant<br>Dog Tasks</div>
  <div class="course__incl">☆ Included In Subscription ☆</div>
  <div class="course__meta"><span>▭ Online</span><span>◎ Certificate</span></div>
  <a class="btn btn--teal">See course detail</a>
</div>
<div class="course" style="left:489px;top:2161px">
  <div class="photo course__img" style="position:relative;background:linear-gradient(180deg,#c8d4de,#9aa0a6)" role="img" aria-label="Trainer walking a dog through an airport terminal"><span class="course__price">$500</span></div>
  <div class="course__title">Public<br>Access</div>
  <div class="course__incl">☆ Included In Subscription ☆</div>
  <div class="course__meta"><span>▭ Online</span><span>◎ Certificate</span></div>
  <a class="btn btn--teal">See course detail</a>
</div>
<div class="course" style="left:729px;top:2161px">
  <div class="photo course__img" style="position:relative;background:linear-gradient(180deg,#d2cfca,#6a5a50)" role="img" aria-label="Handlers kneeling with their dogs"><span class="course__price">$850</span></div>
  <div class="course__title">The<br>Clients</div>
  <div class="course__incl">☆ Included In Subscription ☆</div>
  <div class="course__meta"><span>▭ Online</span><span>◎ Certificate</span></div>
  <a class="btn btn--teal">See course detail</a>
</div>

<section class="section book-band"></section>
<div class="abs book__spine" role="img" aria-label="Open book pages seen from the side"></div>
<div class="abs book__cover" role="img" aria-label="Cover of a service dog training book showing a retriever in a red vest"></div>
<div class="abs reviews">
  <div class="reviews__title">Customer reviews</div>
  <div class="stars">
    <span><svg width="16" height="16" viewBox="0 0 24 24" fill="#fff"><path d="M12 2l3 7 7 .6-5.3 4.6 1.6 7.3L12 17.8 5.7 21.5l1.6-7.3L2 9.6 9 9z"/></svg></span>
    <span><svg width="16" height="16" viewBox="0 0 24 24" fill="#fff"><path d="M12 2l3 7 7 .6-5.3 4.6 1.6 7.3L12 17.8 5.7 21.5l1.6-7.3L2 9.6 9 9z"/></svg></span>
    <span><svg width="16" height="16" viewBox="0 0 24 24" fill="#fff"><path d="M12 2l3 7 7 .6-5.3 4.6 1.6 7.3L12 17.8 5.7 21.5l1.6-7.3L2 9.6 9 9z"/></svg></span>
    <span><svg width="16" height="16" viewBox="0 0 24 24" fill="#fff"><path d="M12 2l3 7 7 .6-5.3 4.6 1.6 7.3L12 17.8 5.7 21.5l1.6-7.3L2 9.6 9 9z"/></svg></span>
    <span><svg width="16" height="16" viewBox="0 0 24 24" fill="none" stroke="#fff" stroke-width="2"><path d="M12 2l3 7 7 .6-5.3 4.6 1.6 7.3L12 17.8 5.7 21.5l1.6-7.3L2 9.6 9 9z"/></svg></span>
  </div>
  <div class="reviews__score">4.7 out of 5</div>
  <div class="reviews__market">bookmarket</div>
</div>
<h3 class="abs book__title">New book from<br>Marianne Holloway Ph.D.!</h3>
<p class="abs book__text">Choosing And Raising Your Assistance Dog: A Field Guide to Public Access.</p>
<a class="btn btn--blue" style="left:626px;top:2773px;width:113px;height:26px">Buy now</a>

<h2 class="h2" style="top:2871px;font-size:24px">Staying Ahead</h2>
<p class="sub" style="top:2929px;color:var(--blue);font-size:11.5px">Science-based and ethical training methods for the modern service dog trainer.</p>
<a class="btn btn--teal" style="left:482px;top:2960px;width:112px;height:26px">Get started</a>
<a class="btn btn--blue" style="left:606px;top:2960px;width:112px;height:26px">Contact us</a>

<footer class="section footer">
  <div class="abs footer__brand"><span class="brand__dot" style="background:var(--white);width:38px;height:38px"></span><span class="brand__name">Brightpath<br>Mentor Center</span></div>
  <p class="abs footer__about">Lorem ipsum dolor sit amet, consectetur adipisicing elit, sed do eiusmod tempor incididunt ut labore et dolore magna aliqua. Ut enim ad minim veniam, quis nostrud exercitation ullamco laboris nisi ut aliquip ex ea commodo conse-</p>
  <div class="abs socials"><span></span><span></span><span></span><span></span></div>
  <ul class="links" style="left:606px">
    <li>About Us</li><li>Marianne Holloway Ph.D.</li><li>Events</li><li>Helping Organizations</li><li>Consulting</li><li>Seminar</li><li>International Coaching</li>
  </ul>
  <ul class="links" style="left:846px">
    <li>What You Need</li><li>Teaching Trainers</li><li>Courses</li><li>Research</li><li>Contact Us</li><li>Privacy Policy</li><li>Cookies Policy</li>
  </ul>
</footer>
<div class="section bottom">
  <span class="abs" style="left:250px;top:8px">© Copyright 2021. All Right Reserved.</span>
  <span class="abs" style="right:249px;top:8px">Designed &amp; Developed By Northgate Studio</span>
</div>

</body>
</html>
```